Local ,start-up premium ice cream brand needs premium packaging sticker design for ice cream tubs

I am a start-up, local premium ice cream brand that needs ice cream packaging sticker designs for ice cream tubs. I currently have 8 flavours - 6 Diary and 2 vegan. I would need space on the design to put a bar code, ingredient list as well as customer company information: Marlow's Ice Cream, www.tenvaricecream.co.za, Email: info@tenvaricecream.co.za, Customer Care Line and Orders: 071 583 9246.
About: Marlow's Ice Cream is ultra-premium, small-batch ice cream made from local ingredients.
I have had my Logo Designed by someone on Pixel Harbor - I can upload them.

Target Market(s)

High earning adults who appreciate and value quality

Font styles to use
Sans Serif

Requirements
Must have
• This design will be printed out in a sticker format and go around an ice cream tub.
It must look premium, luxury, clean and refined and it must also stand out from other ice cream competitors.
Dairy Flavours: Vanilla, Cookies&Cream, Coffee&Dark Chocolate, Salted Caramel, Cinnamon Butter Toast, Belgian Dark Chocolate
Vegan Flavours: Creamy Coffee, Salted Caramel

```html
<!DOCTYPE html>
<html lang="en">
<head>
<meta charset="utf-8">
<title>Marlow's Ice Cream – Cookies &amp; Cream Tub Label</title>
<link rel="stylesheet" href="https://fonts.googleapis.com/css2?family=Montserrat:wght@400;600&family=Playfair+Display:wght@500&display=swap">
<style>
  :root {
    --backdrop: #241010;
    --maroon: #4a0000;
    --maroon-ink: #5c0505;
    --gold: #d9ad4a;
    --gold-light: #f0c860;
    --gold-line: #7a5418;
    --band: #dcdcdc;
    --scoop-light: #efece6;
    --scoop-mid: #cfcac2;
  }
  * { margin: 0; padding: 0; box-sizing: border-box; }
  html, body { width: 1200px; height: 690px; overflow: hidden; }
  body { background: var(--backdrop); position: relative; }

  .tub-label {
    position: absolute;
    left: 40px; top: 44px;
    width: 1121px; height: 611px;
    background: var(--maroon);
    overflow: hidden;
  }
  .flavour-band {
    position: absolute;
    left: 0; top: 222px;
    width: 100%; height: 213px;
    background: var(--band);
    border-top: 8px solid var(--gold-line);
    border-bottom: 8px solid var(--gold-line);
  }
  .brand-oval {
    position: absolute;
    left: 335px; top: 26px;
    width: 430px; height: 290px;
    border-radius: 50%;
    background: var(--maroon);
    border: 6px solid var(--gold-light);
    box-shadow: 0 0 0 1px #a77b22;
    text-align: center;
    color: var(--gold);
    font-family: "Montserrat", sans-serif;
    font-weight: 600;
    z-index: 2;
  }
  .brand-mark {
    position: absolute;
    left: 50%; top: 40px;
    width: 64px; height: 64px;
    margin-left: -32px;
    border: 4px solid var(--gold);
    border-radius: 50%;
  }
  .brand-name {
    position: absolute;
    left: 0; right: 0; top: 118px;
    font-size: 46px;
    line-height: 1;
    letter-spacing: -0.5px;
  }
  .brand-sub {
    position: absolute;
    left: 0; right: 0; top: 168px;
    font-size: 36px;
    line-height: 1;
  }
  .brand-place {
    position: absolute;
    left: 0; right: 0; top: 218px;
    font-size: 15px;
    font-weight: 400;
    letter-spacing: -0.2px;
  }
  .scoop-photo {
    position: absolute;
    left: 770px; top: 318px;
    width: 351px; height: 293px;
    background: radial-gradient(circle at 60% 55%, var(--scoop-light) 0%, var(--scoop-mid) 75%, #b9b3aa 100%);
    clip-path: polygon(110px 6px, 190px 0, 290px 18px, 351px 38px, 351px 293px, 12px 293px, 0 198px, 20px 138px, 60px 100px, 100px 82px, 106px 40px);
    z-index: 1;
  }
  .flavour-name {
    position: absolute;
    left: 228px; top: 318px;
    font-family: "Playfair Display", serif;
    font-weight: 500;
    font-size: 80px;
    line-height: 1;
    color: var(--maroon-ink);
    white-space: nowrap;
    z-index: 3;
  }
</style>
</head>
<body>
  <section class="tub-label">
    <div class="flavour-band"></div>

    <div class="brand-oval">
      <span class="brand-mark"></span>
      <div class="brand-name">Marlow's</div>
      <div class="brand-sub">Ice Cream</div>
      <div class="brand-place">Midlands, South Africa</div>
    </div>

    <div class="scoop-photo" role="img" aria-label="Photo of a scoop of cookies and cream ice cream with dark cookie pieces"></div>

    <h1 class="flavour-name">Cookies &amp; Cream</h1>
  </section>
</body>
</html>
```